Rex Tollbridge (Burn The Stack) CD Cover Design

Professional Cd cover design needed. No photo of the artist necessary for this cover. You can search Rex Tollbridge on YouTube for a feel of the artist, inspiration, etc. Song (Burn The Stack)!

Target Market(s)

Big money makers , Hustlers, those who don't mind spending cash.

Colors

Designer to choose colors to be used in the design.

Requirements
Nice to have
• Any symbols related to money.

```html
<!DOCTYPE html>
<html lang="en">
<head>
<meta charset="utf-8">
<title>Burn The Stack – CD Cover Design</title>
<link rel="stylesheet" href="https://fonts.googleapis.com/css2?family=Pirata+One&display=swap">
<style>
  :root {
    --backdrop: #ef8262;
    --navy: #15205a;
    --navy-deep: #0f1848;
    --teal: #2f8a9a;
    --magenta: #c8356e;
    --gold: #e4b24a;
    --violet: #5a3c8c;
    --hub-grey: #6a6a6e;
    --hub-ring: #d8d8d8;
    --white: #ffffff;
  }
  html, body {
    margin: 0;
    padding: 0;
    width: 1113px;
    height: 1200px;
    overflow: hidden;
    background: var(--backdrop);
  }
  .canvas {
    position: relative;
    width: 1113px;
    height: 1200px;
  }
  .cover {
    position: absolute;
    background: linear-gradient(180deg, var(--navy-deep) 0%, var(--navy) 55%, var(--navy-deep) 100%);
    overflow: hidden;
  }
  .cover--back { left: 140px; top: 174px; width: 390px; height: 384px; }
  .cover--front { left: 579px; top: 176px; width: 440px; height: 382px; }

  .title {
    position: absolute;
    left: 0; right: 0;
    margin: 0;
    text-align: center;
    font-family: "Pirata One", cursive;
    font-weight: 400;
    color: var(--white);
    letter-spacing: 1px;
    line-height: 1;
    white-space: nowrap;
    z-index: 2;
  }
  .cover--back .title { top: 166px; font-size: 54px; }
  .cover--front .title { top: 34px; font-size: 56px; }

  .artwork { position: absolute; }
  .artwork--ribbon {
    background:
      radial-gradient(ellipse 22% 38% at 26% 48%, rgba(228,178,74,0.55), transparent 100%),
      radial-gradient(ellipse 30% 30% at 12% 62%, rgba(200,53,110,0.55), transparent 100%),
      radial-gradient(ellipse 28% 26% at 80% 56%, rgba(200,53,110,0.45), transparent 100%),
      radial-gradient(ellipse 55% 45% at 50% 50%, rgba(47,138,154,0.35), transparent 100%);
  }
  .artwork--teal-field {
    background:
      radial-gradient(ellipse 60% 55% at 30% 70%, rgba(47,138,154,0.6), transparent 100%),
      radial-gradient(ellipse 55% 50% at 75% 55%, rgba(47,138,154,0.5), transparent 100%);
  }
  .artwork--particle-field {
    background:
      radial-gradient(ellipse 40% 22% at 55% 22%, rgba(228,178,74,0.6), transparent 100%),
      radial-gradient(ellipse 70% 45% at 50% 40%, rgba(200,53,110,0.55), transparent 100%),
      radial-gradient(ellipse 80% 70% at 50% 85%, rgba(90,60,140,0.6), transparent 100%);
  }
  .cover--back .artwork--ribbon { left: -20px; top: 10px; width: 430px; height: 160px; }
  .cover--back .artwork--teal-field { left: -20px; top: 200px; width: 430px; height: 200px; }
  .cover--front .artwork--ribbon { left: -20px; top: 90px; width: 480px; height: 150px; }
  .cover--front .artwork--particle-field { left: -20px; top: 200px; width: 480px; height: 200px; }

  .disc {
    position: absolute;
    left: 380px; top: 754px;
    width: 344px; height: 344px;
  }
  .disc__title {
    font-family: "Pirata One", cursive;
    font-size: 42px;
    fill: var(--white);
  }
</style>
</head>
<body>
<main class="canvas">
  <section class="cover cover--back">
    <div class="artwork artwork--ribbon" role="img" aria-label="Flowing ribbon of light in teal, magenta and gold"></div>
    <div class="artwork artwork--teal-field" role="img" aria-label="Rolling field of teal particles"></div>
    <h1 class="title">Burn The Stack</h1>
  </section>

  <section class="cover cover--front">
    <div class="artwork artwork--ribbon" role="img" aria-label="Flowing ribbon of light in teal, magenta and gold"></div>
    <div class="artwork artwork--particle-field" role="img" aria-label="Glowing field of magenta and gold particles with rising rings"></div>
    <h2 class="title">Burn The Stack</h2>
  </section>

  <svg class="disc" viewBox="0 0 344 344" aria-label="Disc label">
    <defs>
      <clipPath id="disc-shape"><circle cx="172" cy="172" r="172"/></clipPath>
      <linearGradient id="disc-base" x1="0" y1="0" x2="0" y2="1">
        <stop offset="0" stop-color="#0f1848"/>
        <stop offset="0.55" stop-color="#15205a"/>
        <stop offset="1" stop-color="#0f1848"/>
      </linearGradient>
      <radialGradient id="disc-ribbon-warm" cx="0.5" cy="0.5" r="0.5">
        <stop offset="0" stop-color="#e4b24a" stop-opacity="0.55"/>
        <stop offset="0.5" stop-color="#c8356e" stop-opacity="0.4"/>
        <stop offset="1" stop-color="#c8356e" stop-opacity="0"/>
      </radialGradient>
      <radialGradient id="disc-ribbon-cool" cx="0.5" cy="0.5" r="0.5">
        <stop offset="0" stop-color="#2f8a9a" stop-opacity="0.4"/>
        <stop offset="1" stop-color="#2f8a9a" stop-opacity="0"/>
      </radialGradient>
      <radialGradient id="disc-particles" cx="0.5" cy="0.5" r="0.5">
        <stop offset="0" stop-color="#e4b24a" stop-opacity="0.55"/>
        <stop offset="0.35" stop-color="#c8356e" stop-opacity="0.5"/>
        <stop offset="0.7" stop-color="#5a3c8c" stop-opacity="0.45"/>
        <stop offset="1" stop-color="#5a3c8c" stop-opacity="0"/>
      </radialGradient>
    </defs>
    <g clip-path="url(#disc-shape)">
      <rect width="344" height="344" fill="url(#disc-base)"/>
      <g role="img" aria-label="Flowing ribbon of light">
        <ellipse cx="200" cy="170" rx="180" ry="50" fill="url(#disc-ribbon-cool)"/>
        <ellipse cx="100" cy="165" rx="110" ry="45" fill="url(#disc-ribbon-warm)"/>
        <ellipse cx="290" cy="150" rx="90" ry="30" fill="url(#disc-ribbon-warm)"/>
      </g>
      <ellipse cx="172" cy="300" rx="230" ry="110" fill="url(#disc-particles)" role="img" aria-label="Glowing particle field"/>
    </g>
    <text class="disc__title" x="172" y="94" text-anchor="middle">Burn The Stack</text>
    <circle cx="172" cy="172" r="51" fill="var(--hub-grey)"/>
    <circle cx="172" cy="172" r="25" fill="var(--hub-ring)"/>
    <circle cx="172" cy="172" r="22" fill="var(--white)"/>
  </svg>
</main>
</body>
</html>
```